Wordpress website design needed for website re-launch of established lawn care company (Design mu...

We are a gardening company and are separating and re-launching the lawn care part of the company. We already have a non-wordpress website which includes a lawn care section and therefore contains all the content needed for the new website. We essentially need to take that content (over 6 pages) and re-create it into a new, modern and visually appealing design in our new Wordpress website. We use Veko and therefore the new design must be built and be compatible with the Veko theme. However, I am not looking to use a pre-built Veko layout or any template offered by Marrow Studio. I could easily do that myself. I'm looking for a bespoke design.

The pages of our current website that need to be re-designed within Veko are:
http://www.brambleworth.co.uk/lawncare/4593693096
http://www.brambleworth.co.uk/lawnfertilisers/4593712410
http://www.brambleworth.co.uk/lawnaeration/4593746736
http://www.brambleworth.co.uk/lawnscarification/4593747084
http://www.brambleworth.co.uk/lawntreatments/4593757226
http://www.brambleworth.co.uk/lawncarepackages/4593712492

Our Wordpress site is already set up with Hostara with the domain www.brambleworthlawns.co.uk and as I say, uses the Veko theme. I am not sure how you will deliver your designs but it must be using or compatible with Veko.

Target Market(s)

Homeowners ages 30+

Industry/Entity Type

Gardener

Font styles to use
Sans Serif

Colors
a64599
9bcb3c

Requirements
Must have
• The new site must still use our existing company colours - purple and green. Have a look on www.brambleworth.co.uk to get the right colours.
• Must be mobile responsive
Nice to have
• We want a fresh and modern new look for our new lawn care website.
• I have also attached a picture of our van and lawn care flyers so you can see what our current branding and style looks like in case it helps with your design.
Should not have
• Please don't just submit pre-designed templates that bear no relevance to my brief or requirements above. I could very easily go and install a pre-designed template and plug my content in but that's not what I'm looking for. Submissions should take into consideration my existing content, my brand colours and my logo as a minimum.

```html
<!DOCTYPE html>
<html lang="en">
<head>
<meta charset="utf-8">
<title>Lawn Fertilisers – Brambleworth Gardening Services</title>
<link href="https://fonts.googleapis.com/css2?family=Roboto:wght@400;500;700&display=swap" rel="stylesheet">
<style>
:root{
  --purple:#7a2381;
  --purple-band:#7d2a86;
  --green:#139a4b;
  --green-light:#3db54a;
  --photo-green-a:#4f8f32;
  --photo-green-b:#7bb845;
  --text:#3a3a3a;
  --grey-band:#f2f2f2;
  --soil:#5b3418;
  --soil-dark:#4a2a12;
  --white:#ffffff;
}
*{box-sizing:border-box;margin:0;padding:0}
html,body{width:1200px;height:4329px;overflow:hidden}
body{position:relative;background:var(--white);font-family:'Roboto',sans-serif;color:var(--text)}
.abs{position:absolute}

/* navigation */
.main-nav{position:absolute;top:21px;left:0;width:1200px;display:flex;justify-content:center;z-index:5}
.main-nav a{font-size:15px;font-weight:500;color:#222;text-decoration:none;margin:0 15px}

/* hero */
.hero{position:absolute;top:0;left:0;width:1200px;height:720px}
.brand{position:absolute;top:92px;left:195px;display:flex;align-items:center;gap:12px;z-index:4}
.brand-dot{width:22px;height:22px;border-radius:50%;background:var(--green-light);flex:none}
.brand-name{font-size:30px;font-weight:500;color:var(--purple);line-height:1.1}
.hero-title{position:absolute;top:305px;left:0;width:1200px;text-align:center;color:var(--white);z-index:4}
.hero-title h1{font-size:38px;font-weight:500;margin-bottom:14px}
.hero-title p{font-size:14px;line-height:23px;width:450px;margin:0 auto}

/* content */
.section-title{font-size:33px;font-weight:500;color:var(--purple);margin-bottom:12px}
.copy p{font-size:13.6px;line-height:23px;margin-bottom:23px}
.copy p:last-child{margin-bottom:0}
.photo{background:linear-gradient(160deg,var(--photo-green-b),var(--photo-green-a))}
.photo-circle{position:absolute;border-radius:50%;border:14px solid var(--white);box-shadow:0 10px 30px rgba(0,0,0,.18)}
.photo-rect{position:absolute;box-shadow:0 25px 40px rgba(0,0,0,.18)}
.grey-band{position:absolute;top:2220px;left:0;width:1200px;height:625px;background:var(--grey-band)}

/* footer */
.footer-brand{position:absolute;top:3965px;left:143px;display:flex;align-items:center;gap:12px}
.footer-brand .brand-name{color:var(--white)}
.footer-col h3{font-size:23px;font-weight:500;color:var(--white);margin-bottom:6px}
.footer-col a,.footer-col p{display:block;font-size:14px;line-height:25px;color:#f3ece6;text-decoration:none}
.contact-line{display:flex!important;align-items:center;gap:8px}
.socials{display:flex;gap:8px;margin-top:10px}
.socials span{width:24px;height:24px;border-radius:50%;background:#5a6fc0}
.socials span:nth-child(2){background:#2aa3e0}
.socials span:nth-child(3){background:#d83a3a}
.socials span:nth-child(4){background:#2a78b8}
.copyright{position:absolute;top:4280px;left:0;width:1200px;text-align:center;font-size:13.5px;color:var(--white)}
.to-top{position:absolute;top:4239px;left:1123px;width:40px;height:40px;border-radius:50%;background:var(--green-light);display:flex;align-items:center;justify-content:center}
</style>
</head>
<body>

<section class="hero">
  <svg width="1200" height="720" viewBox="0 0 1200 720" class="abs" style="top:0;left:0">
    <defs>
      <linearGradient id="heroPhoto" x1="0" y1="0" x2="1" y2="1">
        <stop offset="0" stop-color="#456f2e"/>
        <stop offset="1" stop-color="#6fa83e"/>
      </linearGradient>
    </defs>
    <rect width="1200" height="720" fill="#fff"/>
    <g role="img" aria-label="Photograph of a striped lawn with a path, trees and flowering shrubs">
      <rect x="0" y="60" width="1200" height="620" fill="url(#heroPhoto)"/>
    </g>
    <path d="M0 0 H1200 V40 C1000 40 850 60 700 120 C520 200 330 300 180 280 C90 268 30 210 0 170 Z" fill="#fff"/>
    <path d="M0 125 C40 200 110 270 210 285 C360 305 560 180 810 67 C600 140 420 250 230 255 C120 258 50 200 0 150 Z" fill="var(--purple-band)"/>
    <path d="M810 67 C600 160 420 270 230 285" stroke="#fff" stroke-width="6" fill="none"/>
    <path d="M0 580 C120 470 320 420 520 470 C760 530 950 620 1200 600 V720 H0 Z" fill="var(--purple-band)"/>
    <path d="M0 575 C120 465 320 415 520 462 C760 520 960 600 1200 560 V680 C960 660 760 610 520 540 C320 480 120 520 0 620 Z" fill="var(--green)"/>
    <path d="M0 572 C140 450 340 420 540 500 C720 570 900 650 1200 650 V720 H0 Z" fill="#fff"/>
  </svg>

  <nav class="main-nav">
    <a href="#">Home</a><a href="#">About</a><a href="#">Residential Services</a><a href="#">Lawncare</a><a href="#">Grounds Maintenance</a><a href="#">Garden Advice</a><a href="#">Gallery</a><a href="#">Contact</a>
  </nav>

  <div class="brand">
    <span class="brand-dot"></span>
    <span class="brand-name">Brambleworth<br>Gardening Services</span>
  </div>

  <div class="hero-title">
    <h1>Lawn Fertilisers</h1>
    <p>Our wide range of superior-quality professional fertilisers will ensure your lawn looks lush, green and healthy all year round.</p>
  </div>
</section>

<section class="spring">
  <div class="abs copy" style="top:650px;left:86px;width:530px">
    <h2 class="section-title">Spring Treatment</h2>
    <p>Spring is such a special time of year in the garden. Plants use a lot of energy bringing themselves back to life, and your lawn is no different.  To give it the best possible start, your lawn needs a careful balance of nutrients and to support this, we have chosen what we believe are the best spring fertilisers on the market today.</p>
    <p>As we come into spring, we can assess how your lawn has coped over the winter and can establish if your lawn has any issues that need tending to, such as moss, for example. In having several different fertilisers at our disposal, it means we can tailor our treatment to your lawns exact needs rather than just provide a ‘one size fits all’ product.  It means peace of mind for you knowing that you’re getting the very best treatment available for your lawn, not just the average lawn.</p>
    <p>Our specialist spring fertiliser has been formulated to have the ideal balance of nutrients to strengthen the turf at the beginning of the season.  The high phosphate and potash levels encourage stronger growth and better root development which is so important at this early time of year and sets the way for a healthy lawn all year round.</p>
    <p>In addition, it contains iron to control any moss you might have.  A few days after application, the moss will change colour and require removal. This can be achieved by raking it out, or the most effective and beneficial method is by scarification which is a service we can provide as a one-off treatment or as part of one of our lawn care packages.</p>
    <p>Finally, we apply a weed-killer which selectively controls a wide range of common lawn weeds without causing stress or damage to your lawn.</p>
    <p>It is the perfect treatment for spring and will give your lawn the best possible start to the year.</p>
  </div>
  <div class="photo-circle photo" role="img" aria-label="Photograph of a fertiliser spreader on a lawn" style="top:638px;left:641px;width:462px;height:462px"></div>
  <div class="photo-circle photo" role="img" aria-label="Close-up photograph of lush green grass" style="top:989px;left:699px;width:356px;height:356px"></div>
</section>

<section class="early-summer">
  <div class="photo-rect photo" role="img" aria-label="Photograph of a lawn mower on a green lawn" style="top:1477px;left:173px;width:370px;height:567px"></div>
  <div class="photo-rect photo" role="img" aria-label="Photograph of a person mowing a lawn" style="top:1776px;left:89px;width:256px;height:358px;background:linear-gradient(160deg,#3f7a34,#5a9a3a)"></div>
  <div class="abs copy" style="top:1506px;left:593px;width:522px">
    <h2 class="section-title">Early Summer Treatment</h2>
    <p>Our specialist organic fertiliser has been formulated to meet the specific needs of a lawn in summer and contains the perfect balance of nutrients to create the healthiest, greenest of lawns.</p>
    <p>Firstly, it contains a very effective composting bacteria which breaks down moss and organic matter and turns it into valuable nutrients that continue to feed your turf. This is especially useful at this time of year as it is an effective way of removing any last traces of moss after your spring treatment but doesn’t require any scarification afterwards.</p>
    <p>It uses a similar rate of organic nitrogen as our Spring Fertiliser to ensure the grass isn’t over stimulated in this growing phase and boasts the perfect balance of phosphorus to promote root development and overall health. The high levels of potassium are crucial at this time of year, promoting strong cell membranes and improving your lawn’s tolerance to stress from the heat of the summer, traffic and wear on your lawn and disease. With 3% of magnesium, it provides a noticeably healthy and intense green colour to your lawn, and with ideal levels of calcium, useful for helping respiration during periods of heat and humidity, you can be sure your lawn is receiving the highest quality treatment available today.</p>
  </div>
</section>

<div class="grey-band"></div>
<section class="late-summer">
  <div class="abs copy" style="top:2336px;left:87px;width:520px">
    <h2 class="section-title">Late Summer Treatment</h2>
    <p>Our early and late summer organic fertilisers were formulated in conjunction with award winning sports facilities and as a product, is recognised as being the best summer fertiliser available by turf managers around the world.</p>
    <p>With the heat of the summer slowing growth down, it contains a much needed increased level of nitrogen and a perfectly balanced level of phosphorus and potassium. All of which help your grass withstand the stresses of summer while promoting strength, density and leaf stem growth.</p>
    <p>Our late summer treatment benefits from added magnesium and iron for added vigour and colour and also has the advantage of 25% organic matter derived from meat and bone meal, feather meal and cocoa shells. These, together with many other added trace elements, offer additional benefits to your lawn than the standard nutrients found in fertilisers. They support the entire soil food web which builds a healthy environment which in turn feeds the plant.</p>
  </div>
  <div class="photo-circle photo" role="img" aria-label="Photograph of a freshly mown bright green lawn" style="top:2301px;left:659px;width:464px;height:464px"></div>
</section>

<section class="autumn-winter">
  <div class="photo-rect photo" role="img" aria-label="Photograph of purple allium flowers in a garden border" style="top:2941px;left:111px;width:422px;height:583px;box-shadow:none;background:linear-gradient(180deg,#4f7a34,#3f6630)"></div>
  <div class="abs copy" style="top:2948px;left:593px;width:522px">
    <h2 class="section-title">Autumn / Winter Treatment</h2>
    <p>With the colder days drawing in and the garden preparing to sleep, our slow release Autumn / Winter fertiliser has been chosen specifically to provide a superior level of nutrient support to your lawn to see it through the winter period and back into Spring. Unlike other lawn treatment companies who apply a separate treatment in both Autumn and Winter (and charge you accordingly), we have chosen what is widely accepted as the elite of autumn/winter feeds and thanks to its slow release technology, means that your lawn will continue to benefit from the treatment for 10-12 weeks, making a separate, chargeable treatment unnecessary.</p>
    <p>Using the latest technology, our homogenous fertiliser has been developed to harden and protect your lawn, feeding it gently over a longer period of time to help see it through the winter. It contains a suitably low level of controlled release nitrogen for gentle, longer lasting performance ensuring your lawn is not over stimulated at this time of year. With a measure of phosphate, it assists desirable perennial grasses in building strong root systems in preparation for winter. Importantly, it contains high levels of potassium and sulphur to increase turf hardiness and the ability to resist cold, stress and disease while still maintaining colour. Finally, with traces of iron, magnesium and manganese, it ensures you lawn will continue to maintain a bright green healthy colour over the autumn and winter period and we believe, is the best possible treatment you can give your grass at this time of year making your lawn one to be proud of, all year round.</p>
  </div>
</section>

<footer>
  <svg width="1200" height="760" viewBox="0 3569 1200 760" class="abs" style="top:3569px;left:0">
    <defs>
      <linearGradient id="footerArt" x1="0" y1="0" x2="0" y2="1">
        <stop offset="0" stop-color="#8cc35a"/>
        <stop offset="1" stop-color="#5f9a3c"/>
      </linearGradient>
    </defs>
    <g role="img" aria-label="Illustration of grass growing from the soil">
      <rect x="570" y="3610" width="630" height="280" fill="url(#footerArt)"/>
    </g>
    <path d="M0 3700 C80 3640 170 3600 260 3615 C400 3640 560 3720 760 3790 C930 3850 1080 3880 1200 3880 V4329 H0 Z" fill="var(--soil)"/>
    <path d="M0 3700 C80 3640 170 3600 260 3615 C400 3640 560 3720 760 3790 C930 3850 1080 3880 1200 3880" stroke="var(--soil-dark)" stroke-width="14" fill="none"/>
  </svg>

  <div class="footer-brand">
    <span class="brand-dot"></span>
    <span class="brand-name">Brambleworth<br>Gardening Services</span>
  </div>

  <div class="abs footer-col" style="top:3953px;left:504px;width:240px">
    <h3>Useful Links</h3>
    <a href="#">About</a><a href="#">Residential Services</a><a href="#">Commercial Services</a><a href="#">Lawn Care</a><a href="#">Garden Advice</a><a href="#">Gallery</a><a href="#">Testimonials</a><a href="#">Contact</a><a href="#">Terms &amp; Conditions</a>
  </div>

  <div class="abs footer-col" style="top:3949px;left:795px;width:290px">
    <h3>Contact us for a Quote</h3>
    <p style="line-height:21px;margin-bottom:4px">Whether it be for a one-off job or for regular garden maintenance, contact Martin for a quote.</p>
    <p class="contact-line">
      <svg width="13" height="13" viewBox="0 0 24 24"><path fill="#3db54a" d="M2 5h20v14H2z"/><path d="M2 5l10 8 10-8" stroke="#fff" stroke-width="2" fill="none"/></svg>
      01632 960418
    </p>
    <p class="contact-line">
      <svg width="13" height="13" viewBox="0 0 24 24"><path fill="#3db54a" d="M6.6 10.8a15 15 0 006.6 6.6l2.2-2.2c.3-.3.7-.4 1-.2 1.1.4 2.3.6 3.6.6.6 0 1 .4 1 1V20c0 .6-.4 1-1 1A17 17 0 013 4c0-.6.4-1 1-1h3.5c.6 0 1 .4 1 1 0 1.3.2 2.5.6 3.6.1.3 0 .7-.2 1z"/></svg>
      enquiries@brambleworth.co.uk
    </p>
    <div class="socials"><span></span><span></span><span></span><span></span></div>
  </div>

  <p class="copyright">© Copyright Brambleworth Gardening Services Ltd ®</p>
  <a class="to-top" href="#" aria-label="Back to top">
    <svg width="14" height="14" viewBox="0 0 24 24"><path d="M6 15l6-6 6 6" stroke="#fff" stroke-width="3" fill="none"/></svg>
  </a>
</footer>

</body>
</html>
```